Luxury Eye Cream Label

Velo Skina is developing a line of luxury dermatology creams designed to improve and treat various skin conditions and esthetic problems.
All creams are handmade by registered pharmacies according to patient needs, on the same day of the order. (meaning the creams are not premade. the creams are freshly made without any preservatives or stabilizers.)
The labels are two. One for the upper lid of an aluminum container 4.0 cm. in diameter containing company logo and description of the cream. The other one is for the bottom of the container 4.0 in diameter containing pharmacy information.
The label should convey professional, MD, and luxury feel.
(Upper Lid Label)
Logo of velo skina
EYE CARE CREAM - intensive
Doctor Series
handmade . Doctor formulated . registered Pharmacy . highest ethical standards . (in a circular pattern on the label)
Ingredients: Marigold extract, Witch Hazel Distillate, Water, Glycerin, Stearyl Alcohol, Wheat Germ Oil, Polysorbate 60, Sesame Oil, Myristyl Myristate, Cetyl Alcohol, Sorbitan Stearate, Phenoxyethanol, Calendula Extract, Cornflower Extract, Sodium Alginate, Sodium Citrate, Mica, Vit. C, Vit. E.
Please, adhere to the above content, and dimension of the label of 4 cm in diameter. Also, please view it to scale. This is a relatively small container, aluminum ½ ounce (15ml) cream.
The Bottom of the Jar will have a label with the following information. This is obligatory, because of regulatory requirements for any product prepared by a pharmacy.
I understand that the space is limited. The background should be a lighter color, and the pharmacist will hand write the information (with a darker color marker).
EXTERNAL USE
Pharmacy: Terma, 18 Blvd. Kr. Olvenov, Sofia 1327, ph. 02 4736159
Rx No. Date
Patient Name age
Pharmacist Good until:
Please, view it to scale of 4 cm in diameter (which is the actual label of the Face Cream Intense), so you will have a better feeling of the design.
Thank you so much.

```html
<!DOCTYPE html>
<html lang="en">
<head>
<meta charset="utf-8">
<title>Velo Skina – Eye Care Cream Intensive Lid Label</title>
<link rel="stylesheet" href="https://fonts.googleapis.com/css2?family=Cinzel:wght@400;500&family=PT+Sans:wght@400&family=Herr+Von+Muellerhoff&display=swap">
<style>
  :root {
    --page-bg: #ffffff;
    --label-black: #000000;
    --label-white: #ffffff;
    --brand-gold: #c39a5f;
    --caption-ink: #111111;
  }
  html, body {
    margin: 0;
    padding: 0;
    overflow: hidden;
    background: var(--page-bg);
  }
  .canvas {
    position: relative;
    width: 1200px;
    height: 1000px;
    background: var(--page-bg);
    overflow: hidden;
  }
  .lid-label {
    position: absolute;
    left: 0;
    top: 0;
    width: 1200px;
    height: 1000px;
  }
  .ring-text {
    font-family: "PT Sans", sans-serif;
    font-size: 37px;
    fill: var(--label-white);
  }
  .series-name {
    font-family: "Herr Von Muellerhoff", cursive;
    font-size: 58px;
    fill: var(--label-white);
  }
  .brand-name {
    font-family: "PT Sans", sans-serif;
    font-size: 46px;
    fill: var(--brand-gold);
  }
  .product-line {
    font-family: "Cinzel", serif;
    font-size: 25px;
    letter-spacing: 2px;
    fill: var(--label-white);
  }
  .product-strength {
    font-family: "Cinzel", serif;
    font-size: 38px;
    letter-spacing: 6px;
    fill: var(--label-white);
  }
  .caption {
    position: absolute;
    left: 0;
    top: 784px;
    width: 1200px;
    margin: 0;
    text-align: center;
    font-family: "Cinzel", serif;
    font-size: 27px;
    color: var(--caption-ink);
    letter-spacing: 0.5px;
  }
</style>
</head>
<body>
<main class="canvas">
  <svg class="lid-label" viewBox="0 0 1200 1000" aria-label="Velo Skina eye care cream lid label">
    <defs>
      <path id="ring-path" d="M 382.5 571.4 A 240 240 0 1 1 817.5 368.6 A 240 240 0 1 1 382.5 571.4"/>
    </defs>
    <circle class="label-disc" cx="600" cy="470" r="280" fill="var(--label-black)"/>
    <text class="ring-text">
      <textPath href="#ring-path" textLength="1480" lengthAdjust="spacing">highest ethical standards • handmade • doctor formulated • registered pharmacy •</textPath>
    </text>
    <text class="series-name" x="600" y="408" text-anchor="middle">Doctor Series</text>
    <text class="brand-name" x="600" y="494" text-anchor="middle">velo skina</text>
    <text class="product-line" x="600" y="564" text-anchor="middle">EYE CARE CREAM</text>
    <text class="product-strength" x="600" y="607" text-anchor="middle">INTENSIVE</text>
  </svg>
  <p class="caption">Bottom will be provided after feedback. Thank you!</p>
</main>
</body>
</html>
```